'Cradle Ahead' promotional brochure

We have designed a 6 week program to educate impending first-time parents about the things they need to know to survive the first 6 months. Sessions delivered by general practitioner/family doctor, dietician, physiotherapist, speech pathologist and psychologist. Our promotional blurb is: 'A comprehensive education program for first-time parents-to-be, delivered over 6 weeks by health professionals in your community, about everything you need to know to look after your baby (and yourself!) in the first 6 months'. I now want to put together a promotional brochure to be distributed to those couples who express an interest which will provide further details of what will be delivered in the course.
Updates
In terms of layout, I envisaged a double sided A4 size, foldable into 3 sections, but very happy to be guided on this.
Target Market(s)
To appeal to a young, well educated demographic. First time parents couples.
Industry/Entity Type
Medical
Font styles to use
Other font styles liked:
- Playfair Display
Requirements
Must have
- Playfair display font to be consistent with our logo (attached). Logo also included please. Some consistency with colours of logo please.
Nice to have
- I am a doctor, and have no creative genes! But prefer a clean and professional appearance overall. Not too cluttered in overall appearance.
Should not have
- No cheesy pictures of babies.

```html
<!DOCTYPE html>
<html lang="en">
<head>
<meta charset="utf-8">
<title>Cradle Ahead – Program Brochure</title>
<link href="https://fonts.googleapis.com/css2?family=Arimo:wght@400;700&display=swap" rel="stylesheet">
<style>
  :root{
    --bg:#e9eaec;
    --paper:#ffffff;
    --panel-grey:#ececed;
    --panel-grey-dark:#d9d9db;
    --green:#5aa83a;
    --green-band:#63b045;
    --green-deep:#1f3316;
    --green-light:#dcedcf;
    --text:#3d3d3d;
    --heading:#6a6a6a;
  }
  *{box-sizing:border-box;margin:0;padding:0}
  html,body{width:1200px;height:835px;overflow:hidden;background:var(--bg)}
  body{font-family:"Arimo",Arial,sans-serif;color:var(--text)}
  .brochure{
    position:absolute;left:60px;top:38px;width:1080px;height:760px;
    display:flex;background:var(--paper);overflow:hidden;
    box-shadow:0 14px 30px rgba(0,0,0,.18);
  }
  .panel{width:360px;height:100%;display:flex;flex-direction:column;position:relative}
  .panel + .panel{border-left:1px solid #d6d6d6}
  .week-title{font-size:22px;font-weight:700;color:var(--heading);padding:0 34px;height:62px;flex:none;display:flex;align-items:center;background:var(--paper)}
  .week-title.on-green{color:var(--green)}
  .copy{font-size:13.5px;line-height:1.36;padding:16px 28px 16px 34px;flex:none}
  .name{color:var(--green);font-weight:700}
  .session{color:var(--green);font-weight:700}
  .topics{list-style:none;margin-top:2px}
  .topics li{position:relative;padding-left:14px}
  .topics li::before{
    content:"";position:absolute;left:1px;top:5px;
    border-left:6px solid var(--green);border-top:4px solid transparent;border-bottom:4px solid transparent;
  }
  .copy-week1{background:var(--panel-grey);height:212px}
  .copy-week2{background:var(--green-band);height:285px;color:#263a1c}
  .copy-week2 .session{color:var(--green-deep)}
  .copy-week2 p + p{margin-top:8px}
  .week3{flex:1;display:flex;flex-direction:column;background:linear-gradient(180deg,var(--panel-grey) 0%,var(--panel-grey-dark) 100%);padding-top:4px}
  .week3 .week-title{background:transparent;height:50px}
  .copy-week3{padding-top:4px}
  .copy-week3 p + p{margin-top:12px}
  .copy-week4{background:var(--green-light);height:258px}
  .photo{width:100%}
  .photo-vaccine{height:236px;flex:none;background:linear-gradient(135deg,#cfe4f4 0%,#6fa9d6 45%,#2d6fae 100%)}
  .photo-feeding{flex:1;background:radial-gradient(ellipse at 45% 50%,#e8bfa5 0%,#c99478 55%,#a9735d 100%)}
  .photo-newborn{height:180px;flex:none;background:linear-gradient(160deg,#fbf7f5 0%,#f1d2c3 55%,#e1ad98 100%)}
  .photo-cuddle{flex:1;background:linear-gradient(160deg,#d9d6d4 0%,#e9cdbc 50%,#9a7467 100%)}
</style>
</head>
<body>
  <main class="brochure">
    <section class="panel week1">
      <h2 class="week-title">Week 1</h2>
      <div class="copy copy-week1">
        <p>GP <span class="name">Dr Maren Holloway</span> will share information for Mum's own health after delivery. Topics include:</p>
        <ul class="topics">
          <li>Vaccinations in pregnancy</li>
          <li>Bleeding, bladder and bowel after delivery</li>
          <li>Breastfeeding, engorgement and mastitis</li>
          <li>Bottle feeding</li>
          <li>Post-natal anxiety &amp; depression</li>
          <li>Intimacy and contraception</li>
        </ul>
      </div>
      <div class="photo photo-vaccine" role="img" aria-label="Photo of a gloved hand preparing a vaccine syringe"></div>
      <div class="photo photo-feeding" role="img" aria-label="Close-up photo of a mother breastfeeding her baby"></div>
    </section>

    <section class="panel week2">
      <h2 class="week-title on-green">Week 2</h2>
      <div class="copy copy-week2">
        <p><span class="session">Session 1</span> – Clinical Psychologist Dr Tessa Lindqvist will discuss changes in relationships as couples becomes parents, gender roles in parenting and post-natal depression.</p>
        <p><span class="session">Session 2</span> – Physiotherapist Alina Brooks will present advice for Mums regarding exercise during and after pregnancy, looking after the pelvic floor during and after pregnancy, and abdominal muscle separation management. She will also provide advice for promoting babies' neck strength and minimising the risk of flat spots on the head and encouraging gross motor skills in the first 6 months.</p>
      </div>
      <div class="week3">
        <h2 class="week-title">Week 3</h2>
        <div class="copy copy-week3">
          <p><span class="session">Session 1</span> – Dietician Nora Whitfield provides advice for Mums regarding healthy eating during pregnancy and lactation, normal weight gain during pregnancy and realistic weight loss after. She will also discuss the evidence regarding breastfeeding VS bottle-feeding, normal infant weight gain and introducing solids (including those with potential for allergy).</p>
          <p><span class="session">Session 2</span> – Paediatric Speech Pathologist Clara Moreno will share information about latching and breast-feeding troubles &amp; tongue tie, advice about dummies and finger-sucking, introducing solids &amp; feeding (including 'pouch' food), encouraging language development and current evidence about electronic devices impacting language development.</p>
        </div>
      </div>
    </section>

    <section class="panel week4">
      <h2 class="week-title">Week 4</h2>
      <div class="copy copy-week4">
        <p>GP <span class="name">Dr Maren Holloway</span> will share advice about your babies' health in the first 6 months, including:</p>
        <ul class="topics">
          <li>Skin of newborns</li>
          <li>Sleeping</li>
          <li>Crying</li>
          <li>Immunisations</li>
          <li>Fever and infections</li>
          <li>Diarrhoea and constipation</li>
          <li>Teething</li>
          <li>Understanding a baby's signals</li>
        </ul>
      </div>
      <div class="photo photo-newborn" role="img" aria-label="Photo of a crying newborn baby lying on a white sheet"></div>
      <div class="photo photo-cuddle" role="img" aria-label="Photo of a mother holding her newborn baby close"></div>
    </section>
  </main>
</body>
</html>
```